" Provemos soluções de ITS (Inteligent Transport Systems) para empresas, atuando principalmente na área de concessão rodoviária. Isso inclui sistemas de comunicação via rádio (voz e dados), sistema de monitoramento (CFTV), rede de fibra ótica, analíticos de imagem, dentre outros. A empresa atua na concepção de projetos e na implantação dos mesmos de acordo com a necessidade e operação de nossos clientes. "

```html
<!DOCTYPE html>
<html lang="pt-BR">
<head>
<meta charset="UTF-8">
<title>Rovia Tecnologia — Cartão de visita</title>
<link rel="stylesheet" href="https://fonts.googleapis.com/css2?family=Montserrat:wght@400;500;600;700&display=swap">
<style>
  :root {
    --navy: #0f2f63;
    --blue: #2e8fe0;
    --red: #c62a3c;
    --white: #ffffff;
    --paper-bg: #ebebeb;
    --faint: #e6e8ec;
    --text-light: #dfe8f5;
  }
  * { box-sizing: border-box; margin: 0; padding: 0; }
  html, body {
    width: 1200px; height: 1200px; overflow: hidden;
    background: var(--paper-bg);
    font-family: "Montserrat", sans-serif;
  }
  .sheet {
    width: 1200px; height: 1200px;
    display: flex; flex-direction: column; align-items: center; justify-content: center;
    gap: 60px;
  }
  .card {
    position: relative;
    width: 900px; height: 500px;
    overflow: hidden;
    box-shadow: 0 6px 20px rgba(0,0,0,0.12);
  }
  .edge-stripe {
    position: absolute; left: 0; right: 0; bottom: 34px; height: 10px;
    background: var(--blue);
  }
  .edge-stripe::after {
    content: ""; position: absolute; right: 0; top: 0; bottom: 0; width: 90px;
    background: var(--red);
  }

  /* Front */
  .card-front { background: var(--white); }
  .card-front .backdrop-circle {
    position: absolute; right: 40px; top: -120px;
    width: 420px; height: 420px; border-radius: 50%;
    border: 26px solid var(--faint);
  }
  .card-front .brand {
    position: absolute; left: 50%; top: 50%;
    transform: translate(-50%, -60%);
    display: flex; align-items: center; gap: 18px;
  }
  .brand-dot {
    width: 56px; height: 56px; border-radius: 50%;
    background: var(--blue);
  }
  .brand-name {
    font-weight: 700; color: var(--navy);
    font-size: 58px; letter-spacing: -0.5px;
  }

  /* Back */
  .card-back { background: var(--navy); color: var(--white); }
  .card-back .brand {
    position: absolute; left: 70px; top: 150px;
    display: flex; align-items: center; gap: 14px;
  }
  .card-back .brand-dot { width: 40px; height: 40px; }
  .card-back .brand-name { color: var(--white); font-size: 36px; }
  .person {
    position: absolute; left: 70px; top: 240px;
    display: flex; align-items: flex-start; gap: 14px;
  }
  .icon-box {
    width: 24px; height: 24px; background: var(--blue); border-radius: 3px;
    display: flex; align-items: center; justify-content: center; flex-shrink: 0;
  }
  .icon-box svg { width: 14px; height: 14px; }
  .person-name { font-weight: 600; font-size: 20px; line-height: 24px; }
  .person-role { font-weight: 400; font-size: 16px; color: var(--text-light); margin-top: 2px; }

  .contacts {
    position: absolute; right: 70px; top: 110px;
    display: flex; flex-direction: column; gap: 34px;
  }
  .contact-row {
    display: flex; align-items: flex-start; justify-content: flex-end; gap: 16px;
  }
  .contact-text {
    text-align: right; font-size: 17px; line-height: 24px; color: var(--text-light); font-weight: 500;
  }
</style>
</head>
<body>
<main class="sheet">
  <section class="card card-front">
    <div class="backdrop-circle"></div>
    <div class="brand">
      <span class="brand-dot"></span>
      <span class="brand-name">Rovia Tecnologia</span>
    </div>
    <div class="edge-stripe"></div>
  </section>

  <section class="card card-back">
    <div class="brand">
      <span class="brand-dot"></span>
      <span class="brand-name">Rovia Tecnologia</span>
    </div>

    <div class="person">
      <span class="icon-box">
        <svg viewBox="0 0 14 14"><circle cx="7" cy="4.5" r="2.8" fill="#fff"/><path d="M1.5 13c0-3 2.5-5 5.5-5s5.5 2 5.5 5z" fill="#fff"/></svg>
      </span>
      <div>
        <p class="person-name">Marcelo Tavares</p>
        <p class="person-role">CEO</p>
      </div>
    </div>

    <div class="contacts">
      <div class="contact-row">
        <p class="contact-text">+55 81 98765 4321<br>+55 81 3456 7890</p>
        <span class="icon-box">
          <svg viewBox="0 0 14 14"><path d="M3 1.5l2 .3 1 3-1.4 1.2a8 8 0 0 0 3.4 3.4l1.2-1.4 3 1 .3 2c0 .7-.6 1.5-1.5 1.5A10.5 10.5 0 0 1 1.5 3C1.5 2.1 2.3 1.5 3 1.5z" fill="#fff"/></svg>
        </span>
      </div>
      <div class="contact-row">
        <p class="contact-text">contato@rovia.com.br<br>www.rovia.com.br</p>
        <span class="icon-box">
          <svg viewBox="0 0 14 14"><rect x="1.5" y="3" width="11" height="8" rx="1" fill="#fff"/><path d="M1.8 3.5L7 7.5l5.2-4" stroke="#2e8fe0" stroke-width="1.2" fill="none"/></svg>
        </span>
      </div>
      <div class="contact-row">
        <p class="contact-text">Rua das Palmeiras, 450<br>Centro, Recife-PE</p>
        <span class="icon-box">
          <svg viewBox="0 0 14 14"><path d="M7 1a4 4 0 0 1 4 4c0 3-4 8-4 8S3 8 3 5a4 4 0 0 1 4-4z" fill="#fff"/><circle cx="7" cy="5" r="1.5" fill="#2e8fe0"/></svg>
        </span>
      </div>
    </div>

    <div class="edge-stripe"></div>
  </section>
</main>
</body>
</html>
```